Brochure design for Velicor

Create a bi-fold A5 size brochure. I have attached our logo and the written content to be included in the brochure. So the brochure will have a total of 4 pages (front page, inner two pages, back page). End source files need to include final printable brochure as well as editable files.

```html
<!DOCTYPE html>
<html lang="en">
<head>
<meta charset="utf-8">
<title>Velicor Brochure</title>
<link rel="stylesheet" href="https://fonts.googleapis.com/css2?family=Questrial&display=swap">
<style>
  :root {
    --backdrop: #5d6b60;
    --navy: #0b0d33;
    --navy-deep: #07092a;
    --brand-blue: #2e7fc4;
    --brand-green: #8cc63f;
    --teal: #1a8a86;
    --violet: #6d5a9c;
    --paper: #ffffff;
    --body-text: #3a4a48;
    --muted-text: #7d8a88;
  }
  * { box-sizing: border-box; margin: 0; padding: 0; }
  html, body {
    width: 1200px; height: 1000px; overflow: hidden;
    background: var(--backdrop);
    font-family: "Questrial", "Century Gothic", sans-serif;
  }
  .canvas { position: relative; width: 1200px; height: 1000px; }

  .cover-spread {
    position: absolute; left: 30px; top: 238px;
    width: 740px; height: 523px;
    display: flex;
    box-shadow: 0 10px 30px rgba(0,0,0,.35);
  }
  .panel {
    position: relative; width: 370px; height: 523px;
    background: var(--navy); overflow: hidden;
  }
  .panel--back { background: linear-gradient(90deg, var(--navy-deep), var(--navy)); }
  .panel--front { border-left: 1px solid rgba(255,255,255,.06); }

  .network-pattern { position: absolute; }
  .network-pattern--front {
    right: 0; top: 0; width: 300px; height: 523px;
    background:
      radial-gradient(ellipse at 100% 0%, rgba(26,138,134,.45), transparent 60%),
      radial-gradient(ellipse at 100% 60%, rgba(109,90,156,.35), transparent 55%);
  }
  .network-pattern--back {
    left: 0; bottom: 0; width: 160px; height: 200px;
    background: radial-gradient(ellipse at 0% 100%, rgba(109,90,156,.45), rgba(26,138,134,.2) 45%, transparent 72%);
  }

  .brand {
    position: absolute; display: flex; flex-direction: column; align-items: center;
  }
  .brand__row { display: flex; align-items: center; gap: 8px; }
  .brand__dot { width: 12px; height: 12px; border-radius: 50%; background: var(--brand-green); }
  .brand__name { color: var(--brand-blue); letter-spacing: .5px; line-height: 1; }
  .brand__tagline { color: var(--brand-green); margin-top: 4px; }

  .brand--front { left: 0; right: 0; top: 235px; }
  .brand--front .brand__name { font-size: 44px; }
  .brand--front .brand__tagline { font-size: 11px; }

  .brand--back { left: 0; right: 0; top: 395px; }
  .brand--back .brand__dot { width: 9px; height: 9px; }
  .brand--back .brand__name { font-size: 30px; }
  .brand--back .brand__tagline { font-size: 8px; }
  .brand__web { color: var(--brand-blue); font-size: 11px; margin-top: 14px; letter-spacing: .5px; }

  .inner-page {
    position: absolute; left: 800px; top: 238px;
    width: 370px; height: 523px;
    background: var(--paper); overflow: hidden;
    padding: 26px 26px;
    box-shadow: 0 10px 30px rgba(0,0,0,.35);
    font-size: 9.6px; line-height: 1.36; color: var(--body-text);
  }
  .inner-page__lead {
    color: var(--brand-green); font-size: 11px; line-height: 1.3; margin-bottom: 6px;
  }
  .inner-page__intro { color: var(--muted-text); font-size: 10.5px; margin-bottom: 12px; }
  .inner-page h2 {
    color: var(--teal); font-size: 10.5px; font-weight: 400;
    -webkit-text-stroke: .3px var(--teal); margin: 0 0 2px;
  }
  .inner-page p { margin-bottom: 10px; }
</style>
</head>
<body>
<main class="canvas">
  <section class="cover-spread">
    <div class="panel panel--back">
      <div class="network-pattern network-pattern--back" role="img" aria-label="Connected node network pattern in teal and violet"></div>
      <div class="brand brand--back">
        <div class="brand__row"><span class="brand__dot"></span><span class="brand__name">velicor</span></div>
        <span class="brand__tagline">Personalised Health &amp; Wellness</span>
        <span class="brand__web">www.velicor.co</span>
      </div>
    </div>
    <div class="panel panel--front">
      <div class="network-pattern network-pattern--front" role="img" aria-label="Connected node network pattern in teal and violet"></div>
      <div class="brand brand--front">
        <div class="brand__row"><span class="brand__dot"></span><span class="brand__name">velicor</span></div>
        <span class="brand__tagline">Personalised Health &amp; Wellness</span>
      </div>
    </div>
  </section>

  <article class="inner-page">
    <p class="inner-page__lead">A revolution in health &amp; wellness has been brewing and now it is here!</p>
    <p class="inner-page__intro">Precision health and wellness is tailored to your unique genetic make-up.</p>

    <h2>Precision Health &amp; Wellness</h2>
    <p>You are unique. Your healthcare and lifestyle decisions need to be tailored to you. Ever since the human genome was decoded, a plethora of scientific data has revealed everything from disease-causing genes to genetically tailored diets. We all want to live longer and healthier lives, whilst performing at our peak. One size does not fit all and the only way to find out what's right for you is to unlock your hidden code.</p>

    <h2>DNA – The Code of Life</h2>
    <p>Every individual living organism has a completely unique set of DNA. Your DNA is the chemical blueprint that codes for everything in your body and is found in all of the trillions of cells that you are made of. Collections of DNA are called genes and the complete set of genes in an individual is referred to as their genome. The human genome was first decoded in 2003, taking over 13 years and $2.7 billion to complete! Thanks to exponential advances in technology, Velicor™ can now unlock your DNA for only a fraction of the time and cost.</p>

    <h2>Unlock Your Hidden Code</h2>
    <p>A whole new world of discovery awaits with the Velicor™ range of genetic testing services. From unlocking your complete genome with Whole Genome Sequencing (WGS) to just learning about specific aspects of what makes you – you.</p>
    <p>With Velicor™, you can find answers to the questions that can help you to live a healthier, longer and optimal quality of life.</p>
  </article>
</main>
</body>
</html>
```